Website-Design for a OnePage (no coding) for IT-support

I need a modern and structured design for a vertically scrollable website, so just one page.

Because it is a newly founded business, there is only a logo right now (see attachments). Other design elements can be chosen by you. The name of the company is "Kelvor".

The color codes are:
- dark blue #415c77
- light blue #1c86ee

Please follow these requirements:
- there are five services (Fernwartung mit Anydesk/Computer Instandsetzung/Cloud- Lösungen/Datenwiderherstellung/Upgrade Ihres Betriebssystems). The first one is the most important
- we need a certain space in the top area (on slider, first section or something like that) to show current news
- social media icons should be found
- there is no team, only one person, which should get a certain space to be introduced
- somewhere around the "about me" section we would like to include about 5 logos/certificates
- we will add one subpage, so we need an easy to find Call-To-Action button

At the end I need one image file with a width of 1920px and all design elements as single files.

If you have any questions, feel free to contact me.

```html
<!DOCTYPE html>
<html lang="en">
<head>
<meta charset="utf-8">
<title>Kelvor – IT Support</title>
<link href="https://fonts.googleapis.com/css2?family=Montserrat:wght@400;500;600;700&family=PT+Sans+Narrow:wght@400;700&display=swap" rel="stylesheet">
<style>
:root{
  --blue:#2f72c2;
  --blue-bright:#1c86ee;
  --navy:#435d7b;
  --ink:#2a3442;
  --muted:#7a8290;
  --soft-bg:#f8f8f8;
  --footer:#06090f;
  --white:#ffffff;
}
*{margin:0;padding:0;box-sizing:border-box}
html,body{width:1200px;height:3084px;overflow:hidden}
body{position:relative;background:var(--white);font-family:'Montserrat',sans-serif;color:var(--ink)}
.abs{position:absolute}
.narrow{font-family:'PT Sans Narrow',sans-serif}

/* header */
.site-header{top:0;left:0;width:1200px;height:76px;background:var(--white)}
.brand{display:flex;align-items:center;gap:8px;color:var(--blue);font-family:'PT Sans Narrow',sans-serif;font-weight:700;font-size:36px}
.brand-dot{width:38px;height:38px;border-radius:50%;border:3px solid var(--navy)}
.site-header .brand{position:absolute;left:156px;top:16px}
.divider-v{left:343px;top:26px;width:1px;height:26px;background:#d5d9e0}
.search{left:364px;top:32px;font-size:10px;color:#8a92a0;letter-spacing:.5px;display:flex;gap:6px;align-items:center}
.menu{right:156px;top:32px;font-size:10px;font-weight:600;color:var(--blue);display:flex;gap:8px;align-items:center}

/* hero */
.hero{top:76px;left:0;width:1200px;height:560px;background:linear-gradient(100deg,#5a636c 0%,#3c444d 35%,#59626a 60%,#7a8690 100%)}
.hero-shade{top:76px;left:0;width:1200px;height:560px;background:linear-gradient(180deg,rgba(10,14,22,.15) 0%,rgba(10,14,22,.35) 60%,rgba(6,9,15,.9) 100%)}
.hero-hello{left:591px;top:172px;color:var(--white);font-size:20px}
.hero-name{left:591px;top:198px;color:var(--white);font-size:64px;font-weight:700;letter-spacing:1px;white-space:nowrap}
.hero-lead{left:593px;top:283px;width:370px;color:#e8ecf1;font-size:16.5px;line-height:22px}
.hero-social{left:1104px;top:232px;width:14px;height:250px}
.hero-social span{position:absolute;left:0;writing-mode:vertical-rl;font-size:6.5px;letter-spacing:1.5px;color:var(--white);font-weight:600;white-space:nowrap}
.news-label{left:156px;top:489px;color:var(--white);font-family:'PT Sans Narrow',sans-serif;font-weight:700;font-size:15px}
.news-item{color:var(--white);font-family:'PT Sans Narrow',sans-serif;font-size:12px;line-height:16px;padding:12px 17px}
.news-item .date{display:block;font-size:10px;margin-bottom:8px}
.news-item.active{background:rgba(70,74,82,.75)}
.dots{left:1076px;top:574px;display:flex;gap:6px}
.dots i{width:4px;height:4px;border-radius:50%;background:rgba(255,255,255,.45)}
.dots i:first-child{background:var(--white)}

/* section labels */
.eyebrow{font-size:11px;font-weight:700;color:var(--blue);letter-spacing:.5px;display:flex;align-items:center;gap:10px}
.eyebrow::before{content:"";width:14px;height:2px;background:var(--blue)}
.section-title{font-family:'PT Sans Narrow',sans-serif;font-weight:700;font-size:30px;line-height:33px;color:var(--ink)}

/* about */
.about-text{left:180px;top:836px;width:376px;font-size:14px;line-height:27.3px;color:var(--muted)}
.btn{display:flex;align-items:center;gap:14px;background:var(--blue);color:var(--white);font-family:'PT Sans Narrow',sans-serif;font-size:12px;padding:0 24px;height:40px;border-radius:2px}
.btn.shadow{box-shadow:0 10px 18px rgba(47,114,194,.35)}
.about-frame{left:627px;top:759px;width:417px;height:412px;background:var(--blue)}
.about-photo{left:659px;top:733px;width:353px;height:463px;background:linear-gradient(160deg,#8fbde0 0%,#6f8f70 45%,#3f5c63 75%,#2e4850 100%)}

/* services */
.services-bg{top:1280px;left:0;width:1200px;height:480px;background:var(--soft-bg)}
.service{width:240px}
.service h3{font-family:'PT Sans Narrow',sans-serif;font-weight:700;font-size:12px;margin:16px 0 8px;color:var(--ink)}
.service p{font-size:11.5px;line-height:17.5px;color:var(--muted);width:182px}
.service.featured{background:var(--blue);padding:22px 24px;box-shadow:0 10px 22px rgba(47,114,194,.3)}
.service.featured h3,.service.featured p{color:var(--white)}

/* clients */
.client{width:160px;height:101px;background:var(--white);box-shadow:0 2px 10px rgba(0,0,0,.08);display:flex;align-items:center;justify-content:center;gap:8px;font-family:'Montserrat',sans-serif;font-weight:600;font-size:16px;color:#3b4452}
.client i{width:14px;height:14px;border-radius:50%;background:#3b4452}

/* contact */
.contact{top:2133px;left:0;width:1200px;height:563px;background:var(--navy)}
.center{left:0;width:1200px;text-align:center;color:var(--white)}
.field-label{font-family:'PT Sans Narrow',sans-serif;font-size:12px;color:var(--white)}
.field{background:var(--white);border-radius:2px;font-size:10px;color:#9aa1ab;padding:12px 16px}

/* footer */
.footer{top:2696px;left:0;width:1200px;height:388px;background:var(--footer)}
.footer-links{top:2845px;left:0;width:1200px;display:flex;justify-content:center;gap:22px;font-size:10.5px;font-weight:500;color:var(--white)}
.footer-social{top:2883px;left:0;width:1200px;display:flex;justify-content:center;gap:10px;font-size:7px;letter-spacing:2px;font-weight:600;color:var(--white)}
.footer-rule{left:276px;top:2929px;width:648px;height:1px;background:#1b212b}
.footer-info{top:2952px;font-family:'PT Sans Narrow',sans-serif;font-size:11px;color:var(--white)}
.copyright{top:3024px;left:0;width:1200px;text-align:center;font-size:10px;color:#c8ccd3}
</style>
</head>
<body>

<header class="abs site-header">
  <div class="brand"><span class="brand-dot"></span>Kelvor</div>
  <div class="abs divider-v"></div>
  <div class="abs search">
    <svg width="11" height="11" viewBox="0 0 12 12" fill="none" stroke="#8a92a0" stroke-width="1.4"><circle cx="5" cy="5" r="3.8"/><path d="M8 8l3 3"/></svg>SEARCH
  </div>
  <div class="abs menu">MENU
    <svg width="16" height="11" viewBox="0 0 16 11" stroke="#2f72c2" stroke-width="1.6"><path d="M0 1h16M0 5.5h16M5 10h11"/></svg>
  </div>
</header>

<section>
  <div class="abs hero" role="img" aria-label="Portrait of a bearded man in glasses and a dark jacket on a city street"></div>
  <div class="abs hero-shade"></div>
  <p class="abs hero-hello">Hello</p>
  <h1 class="abs hero-name">I’m Jan Dorn</h1>
  <p class="abs hero-lead">Ut enim ad minim veniam, quis nostrud exercitation ullamco laboris nisi ut aliquip ex ea commodo consequat.</p>
  <div class="abs hero-social">
    <span style="top:0">PAGEHUB</span>
    <span style="top:70px">CHIRPR</span>
    <span style="top:133px">VIDSTREAM</span>
    <span style="top:200px">SNAPGRAM</span>
  </div>
  <p class="abs news-label">Latest News:</p>
  <div class="abs news-item active" style="left:156px;top:524px;width:211px;height:80px"><span class="date">21.10.19</span>Ut enim ad minim veniam, quis nostrud exercitation ullamco</div>
  <div class="abs news-item" style="left:444px;top:524px;width:200px"><span class="date">10.10.19</span>Excepteur sint occaecat cupidatat non proident, sunt in culpa qui</div>
  <div class="abs news-item" style="left:747px;top:524px;width:200px"><span class="date">10.10.19</span>Sed ut perspiciatis unde omnis iste natus error sit voluptatem</div>
  <div class="abs dots"><i></i><i></i><i></i><i></i></div>
</section>

<section>
  <p class="abs eyebrow" style="left:156px;top:713px">ABOUT ME</p>
  <h2 class="abs section-title" style="left:180px;top:757px">A little about me<br>and my works</h2>
  <p class="abs about-text">Sed ut perspiciatis unde omnis iste natus error sit voluptatem accusantium doloremque. laudantium, totam rem aperiam, eaque ipsa quae ab illo inventore veritatis et quasi architecto beatae vitae dicta sunt explicabo. Nemo enim ipsam voluptatem quia voluptas sit aspernatur aut odit aut fugit, sed quia consequuntur magni dolores eos qui ratione voluptatem sequi nesciunt.</p>
  <a class="abs btn shadow" style="left:180px;top:1109px;width:137px">READ MORE
    <svg width="14" height="10" viewBox="0 0 14 10" fill="none" stroke="#fff" stroke-width="1.4"><path d="M0 5h13M9 1l4 4-4 4"/></svg>
  </a>
  <div class="abs about-frame"></div>
  <div class="abs about-photo" role="img" aria-label="Portrait of a young man with long hair outdoors"></div>
</section>

<section>
  <div class="abs services-bg"></div>
  <p class="abs eyebrow" style="left:156px;top:1347px">OUR SERVICES</p>
  <h2 class="abs section-title" style="left:180px;top:1390px">Various type of<br>services</h2>

  <div class="abs service featured" style="left:460px;top:1349px;height:167px">
    <svg width="26" height="22" viewBox="0 0 26 22" fill="none" stroke="#fff" stroke-width="1.5"><rect x="1" y="1" width="18" height="12" rx="2"/><path d="M5 13v5l4-5M7 15h12l4 4v-10h-4"/><path d="M5 6h10M5 9h7"/></svg>
    <h3>VOLUPTATEM</h3>
    <p>Consectetur adipisicing elit, sed do eiusmod ut labore et dolore magna aliqua.</p>
  </div>
  <div class="abs service" style="left:788px;top:1371px">
    <svg width="24" height="24" viewBox="0 0 24 24" fill="none" stroke="#2f72c2" stroke-width="1.5"><path d="M12 2l3 6.5 7 .8-5.2 4.8 1.5 7L12 17.5 5.7 21l1.5-7L2 9.3l7-.8z"/></svg>
    <h3>ACCUSANTIUM</h3>
    <p>Ut enim ad minim veniam, quis nostrud exercitation ullamco laboris nisi ut aliqui.</p>
  </div>
  <div class="abs service" style="left:180px;top:1556px">
    <svg width="24" height="24" viewBox="0 0 24 24" fill="none" stroke="#2f72c2" stroke-width="1.5"><circle cx="12" cy="12" r="10"/><circle cx="12" cy="12" r="6"/><path d="M9 12l2 2 4-4"/></svg>
    <h3>TOTAM</h3>
    <p>Duis aute irure dolor in reprehenderit in voluptate velit esse cillum dolore eu.</p>
  </div>
  <div class="abs service" style="left:485px;top:1556px">
    <svg width="16" height="26" viewBox="0 0 16 26" fill="none" stroke="#2f72c2" stroke-width="1.5"><rect x="1" y="1" width="14" height="24" rx="2"/><path d="M1 5h14M1 20h14M7 22.5h2"/></svg>
    <h3>DOLOREM</h3>
    <p>Excepteur sint occaecat cupidatat non proident, sunt in culpai officia deserunt.</p>
  </div>
  <div class="abs service" style="left:788px;top:1556px">
    <svg width="26" height="24" viewBox="0 0 26 24" fill="none" stroke="#2f72c2" stroke-width="1.4"><circle cx="6" cy="4" r="2.5"/><circle cx="13" cy="4" r="2.5"/><circle cx="20" cy="4" r="2.5"/><path d="M2 22V11a3 3 0 013-3h2a3 3 0 013 3v11M9 22V11a3 3 0 013-3h2a3 3 0 013 3v11M16 22V11a3 3 0 013-3h2a3 3 0 013 3v11"/></svg>
    <h3>AUDANTIUM</h3>
    <p>ex ea commodo consequat. fugiat nulla pariatur. mollit anim id est laborum.</p>
  </div>
  <svg class="abs" style="left:668px;top:1518px" width="14" height="18" viewBox="0 0 14 18" fill="#fff" stroke="#2a3442" stroke-width="1"><path d="M4 8V2.5a1.2 1.2 0 012.4 0V7h0V5.8a1.2 1.2 0 012.4 0V7.5a1.2 1.2 0 012.3 0v1a1.2 1.2 0 012.3 0V13c0 2.5-2 4.5-4.5 4.5H7.5A4 4 0 014 16L1.3 11.3a1.2 1.2 0 012-1.3L4 11z"/></svg>
</section>

<section>
  <p class="abs eyebrow" style="left:156px;top:1824px">MY HONORABLE</p>
  <h2 class="abs section-title" style="left:180px;top:1868px">Clients</h2>
  <div class="abs client" style="left:513px;top:1827px">TALLOW</div>
  <div class="abs client" style="left:697px;top:1827px"><i></i>Brightmoor</div>
  <div class="abs client" style="left:881px;top:1827px">Cedarline</div>
  <div class="abs client" style="left:513px;top:1955px"><i></i>NORWELL</div>
  <div class="abs client" style="left:697px;top:1955px">Oakhaven</div>
</section>

<section>
  <div class="abs contact"></div>
  <div class="abs" style="left:593px;top:2202px;width:14px;height:2px;background:#fff"></div>
  <p class="abs center" style="top:2215px;font-size:11px;font-weight:700;letter-spacing:.5px">CONTACT US</p>
  <h2 class="abs center narrow" style="top:2232px;font-size:32px;font-weight:700">Get in Touch</h2>
  <p class="abs center" style="top:2279px;font-size:14px;color:#eef1f5">Fill up the form below and our expert will contact you soon.</p>

  <p class="abs field-label" style="left:156px;top:2332px">NAME</p>
  <p class="abs field-label" style="left:460px;top:2332px">PHONE NUMBER</p>
  <p class="abs field-label" style="left:764px;top:2332px">EMAIL</p>
  <div class="abs field" style="left:156px;top:2355px;width:280px;height:40px">Type your name</div>
  <div class="abs field" style="left:460px;top:2355px;width:280px;height:40px">Type your phone number</div>
  <div class="abs field" style="left:764px;top:2355px;width:280px;height:40px">Type your email address</div>
  <p class="abs field-label" style="left:156px;top:2416px">YOUR MESSAGE</p>
  <div class="abs field" style="left:156px;top:2440px;width:888px;height:127px">Type your message here...</div>
  <a class="abs btn" style="left:156px;top:2592px;width:137px">SUBMIT NOW
    <svg width="14" height="10" viewBox="0 0 14 10" fill="none" stroke="#fff" stroke-width="1.4"><path d="M0 5h13M9 1l4 4-4 4"/></svg>
  </a>
</section>

<footer>
  <div class="abs footer"></div>
  <div class="abs brand" style="left:522px;top:2754px"><span class="brand-dot"></span>Kelvor</div>
  <nav class="abs footer-links"><span>ABOUT ME</span><span>SERVICES</span><span>LATEST NEWS</span><span>CONTACT</span></nav>
  <div class="abs footer-social"><span>PAGEHUB</span><span>·</span><span>CHIRPR</span><span>·</span><span>VIDSTREAM</span><span>·</span><span>SNAPGRAM</span></div>
  <div class="abs footer-rule"></div>
  <p class="abs footer-info" style="left:276px">Harlow Lane, Brenton, Ohio, 40213</p>
  <p class="abs footer-info" style="left:572px">555-014-2290</p>
  <p class="abs footer-info" style="left:756px">hello@kelvor.com</p>
  <p class="abs copyright">© 2019 Kelvor.com</p>
</footer>

</body>
</html>
```